Welcome Center Signage/logo Design with Multicultural Relevance

We are looking to have a welcome signage/logo designed for our church lobby with either the word "welcome" or "Welcome to the Dunmore Valley Fellowship!"

This design must include our organizational logo (attached). It could (but does not need to) also include our church vision: "Our vision is to be a thriving diverse urban church sharing Christ's love and serving the needs of our local and global communities." The logo/signage will be printed on 4' x 6' stretch fabric.

This signage will then be hung up behind our welcome center...it will be one of the first things people see upon entering our building.

We are an urban multicultural church that has significant outreach into our local community, one that is quite culturally diverse. If you would like more information about our church, please visit www.dunmorevalleyfc.org.
Updates

Project Deadline Extended
Reason: We have committed to continue work with the designers on designs submitted over the last several days, and are scheduling the additional time needed to do so. Thank you!

Target Market(s)

Culturally (African American, Hispanic American, Asian American, European American) diverse millennials and iGens

Industry/Entity Type

Church

Font styles to use
Sans Serif

Requirements
Must have
• Our logo
Nice to have
• "Welcome" in many languages
Should not have
• I can't think of anything at the moment.

```html
<!DOCTYPE html>
<html lang="en">
<head>
<meta charset="utf-8">
<title>Welcome — Dunmore Valley Fellowship</title>
<link rel="stylesheet" href="https://fonts.googleapis.com/css2?family=Archivo:wdth,wght@62..125,100..900&family=Noto+Sans:wght@700&family=Noto+Sans+Thai:wght@500&family=Noto+Sans+Myanmar:wght@500&family=Vazirmatn:wght@600&display=swap">
<style>
  :root {
    --bg-light: #fffdf9;
    --bg-peach: #fbe3c8;
    --bg-amber: #eab26a;
    --bg-rust: #c8743c;
    --welcome-red: #e31b3c;
    --welcome-deep: #c8102e;
    --teal: #27a9b3;
    --navy: #2f3f5c;
    --slate: #5a6a85;
    --wine: #9e2236;
    --red: #d9262c;
    --orange: #f08a1c;
    --light-orange: #f6b676;
    --gold: #f2b81f;
    --mustard: #e3b23c;
    --brown: #93613e;
    --rust-brown: #b35a1f;
    --purple: #7a3a8a;
    --magenta-plum: #8e3672;
    --blue: #3f6ea3;
    --olive: #8c8a4e;
    --thai-grey: #8d9fb4;
    --persian-brown: #7a4a3a;
  }
  html, body {
    margin: 0;
    padding: 0;
    width: 1200px;
    height: 800px;
    overflow: hidden;
    background: var(--bg-light);
  }
  .sign { display: block; width: 1200px; height: 800px; }
  .word {
    font-family: "Archivo", "Noto Sans", sans-serif;
    font-weight: 800;
    font-stretch: 112%;
  }
  .welcome { font-weight: 900; font-stretch: 125%; letter-spacing: -2px; }
  .tagline { font-weight: 800; font-stretch: 125%; fill: var(--teal); }
  .org-name { font-weight: 800; fill: var(--wine); }
  .org-dot { fill: var(--wine); }
  .thai { font-family: "Noto Sans Thai", sans-serif; font-weight: 500; fill: var(--thai-grey); }
  .burmese { font-family: "Noto Sans Myanmar", sans-serif; font-weight: 500; fill: var(--red); }
  .persian { font-family: "Vazirmatn", sans-serif; font-weight: 600; fill: var(--persian-brown); }
  .cyrillic { font-family: "Noto Sans", sans-serif; font-weight: 700; font-stretch: 100%; }
  .c-red { fill: var(--red); }
  .c-wine { fill: var(--wine); }
  .c-navy { fill: var(--navy); }
  .c-slate { fill: var(--slate); }
  .c-orange { fill: var(--orange); }
  .c-light-orange { fill: var(--light-orange); }
  .c-gold { fill: var(--gold); }
  .c-mustard { fill: var(--mustard); }
  .c-brown { fill: var(--brown); }
  .c-rust-brown { fill: var(--rust-brown); }
  .c-purple { fill: var(--purple); }
  .c-plum { fill: var(--magenta-plum); }
  .c-blue { fill: var(--blue); }
  .c-olive { fill: var(--olive); }
  .c-teal { fill: var(--teal); }
  .c-welcome { fill: url(#welcome-fill); }
</style>
</head>
<body>
<svg class="sign" viewBox="0 0 1200 800" xmlns="http://www.w3.org/2000/svg" role="img" aria-label="Welcome to the Dunmore Valley Fellowship, with welcome in many languages">
  <defs>
    <radialGradient id="backdrop-glow" cx="0.45" cy="0.35" r="0.85">
      <stop offset="0" stop-color="var(--bg-light)"/>
      <stop offset="0.55" stop-color="var(--bg-light)"/>
      <stop offset="0.8" stop-color="var(--bg-peach)"/>
      <stop offset="1" stop-color="var(--bg-amber)"/>
    </radialGradient>
    <linearGradient id="backdrop-warmth" x1="0" y1="0" x2="0" y2="1">
      <stop offset="0.55" stop-color="var(--bg-amber)" stop-opacity="0"/>
      <stop offset="0.85" stop-color="var(--bg-amber)" stop-opacity="0.55"/>
      <stop offset="1" stop-color="var(--bg-rust)" stop-opacity="0.8"/>
    </linearGradient>
    <linearGradient id="welcome-fill" x1="0" y1="0" x2="1" y2="1">
      <stop offset="0" stop-color="var(--welcome-deep)"/>
      <stop offset="0.5" stop-color="var(--welcome-red)"/>
      <stop offset="1" stop-color="var(--welcome-deep)"/>
    </linearGradient>
  </defs>

  <rect class="backdrop" width="1200" height="800" fill="url(#backdrop-glow)"/>
  <rect class="backdrop-warmth" width="1200" height="800" fill="url(#backdrop-warmth)"/>

  <g class="org-mark">
    <circle class="org-dot" cx="210" cy="203" r="62"/>
    <text class="word org-name" x="282" y="172" font-size="13" textLength="150" lengthAdjust="spacingAndGlyphs">Dunmore Valley Fellowship</text>
  </g>

  <text class="thai" x="374" y="116" font-size="40" textLength="190" lengthAdjust="spacingAndGlyphs">ยินดีต้อนรับ</text>
  <text class="word c-red" x="480" y="208" font-size="34" textLength="108" lengthAdjust="spacingAndGlyphs">KARIBU</text>
  <text class="word c-wine" x="702" y="208" font-size="29" textLength="184" lengthAdjust="spacingAndGlyphs">WA NAH HAIL</text>
  <text class="word c-brown" x="663" y="258" font-size="50" textLength="274" lengthAdjust="spacingAndGlyphs">BENVIGUT</text>
  <text class="word c-wine" x="280" y="263" font-size="38" textLength="161" lengthAdjust="spacingAndGlyphs">WITAMY</text>
  <text class="word c-teal" x="178" y="295" font-size="15" textLength="199" lengthAdjust="spacingAndGlyphs">HERZLICH WILLKOMMEN</text>
  <text class="word c-blue" x="526" y="314" font-size="58" textLength="420" lengthAdjust="spacingAndGlyphs">BIENVENIDO</text>
  <text class="word c-purple" x="1001" y="310" font-size="23" textLength="173" lengthAdjust="spacingAndGlyphs">BINE AI VENIT</text>

  <text class="word welcome c-welcome" x="186" y="415" font-size="152" textLength="842" lengthAdjust="spacingAndGlyphs">Welcome</text>
  <text class="word tagline" x="210" y="447" font-size="28" textLength="560" lengthAdjust="spacingAndGlyphs">to the Dunmore Valley Fellowship</text>

  <text class="persian" x="178" y="410" font-size="34" text-anchor="end">خوش آمدید</text>

  <text class="word c-plum" x="254" y="512" font-size="58" textLength="392" lengthAdjust="spacingAndGlyphs">BONVENON</text>
  <text class="word c-navy" x="452" y="554" font-size="43" textLength="310" lengthAdjust="spacingAndGlyphs">HOSPEDAR</text>
  <text class="word c-rust-brown" x="805" y="508" font-size="45" textLength="326" lengthAdjust="spacingAndGlyphs">VELKOMMEN</text>
  <text class="word c-light-orange" x="805" y="551" font-size="41" textLength="268" lengthAdjust="spacingAndGlyphs">BIENVENUE</text>
  <text class="word c-orange" x="252" y="600" font-size="43" textLength="318" lengthAdjust="spacingAndGlyphs">MWABONWA</text>
  <text class="burmese" x="254" y="650" font-size="40" textLength="208" lengthAdjust="spacingAndGlyphs">ကြိုဆိုပါတယ်</text>

  <text class="word c-mustard" x="473" y="323" font-size="31" textLength="185" lengthAdjust="spacingAndGlyphs" transform="rotate(-90 473 323)">BENVENUTO</text>
  <text class="word c-navy" x="646" y="254" font-size="36" textLength="212" lengthAdjust="spacingAndGlyphs" transform="rotate(-90 646 254)">BEM VINDO</text>
  <text class="word c-red" x="942" y="203" font-size="23" textLength="166" lengthAdjust="spacingAndGlyphs" transform="rotate(-90 942 203)">HOŞGELDINIZ</text>
  <text class="word c-gold" x="995" y="309" font-size="50" textLength="244" lengthAdjust="spacingAndGlyphs" transform="rotate(-90 995 309)">SWAAGAT</text>
  <text class="word c-brown" x="1097" y="462" font-size="35" textLength="120" lengthAdjust="spacingAndGlyphs" transform="rotate(-90 1097 462)">MAUYA</text>
  <text class="word c-olive" x="163" y="623" font-size="24" textLength="203" lengthAdjust="spacingAndGlyphs" transform="rotate(-90 163 623)">MIRË SE ERDHE</text>
  <text class="word c-navy" x="245" y="720" font-size="47" textLength="254" lengthAdjust="spacingAndGlyphs" transform="rotate(-90 245 720)">RECOGER</text>
  <text class="word c-purple" x="796" y="646" font-size="37" textLength="177" lengthAdjust="spacingAndGlyphs" transform="rotate(-90 796 646)">WELKOM</text>
  <text class="word c-blue" x="642" y="748" font-size="34" textLength="183" lengthAdjust="spacingAndGlyphs" transform="rotate(-90 642 748)">AKWAABA</text>
  <text class="cyrillic c-slate" x="1071" y="729" font-size="22" textLength="170" lengthAdjust="spacingAndGlyphs" transform="rotate(-90 1071 729)">ДОБРО ПОЖАЛОВАТЬ</text>
</svg>
</body>
</html>
```